Tarvimoor business cards

Need fresh design for our business cards. Logo must be specific, we are open for everything else.

Contact Information for Business Card

phrase "GMP & JANITORIAL SERVICES" should be used as main point of card

Colors
3176b5
3276b5
85acd3
cedeed
ffffff
0292cd
33a6d7
85cae6
cee9f5

Requirements
Must have
• The logo
Should not have
• crowded designs

```html
<!DOCTYPE html>
<html lang="en">
<head>
<meta charset="utf-8">
<title>Tarvimoor business cards</title>
<link href="https://fonts.googleapis.com/css2?family=Roboto:wght@300;400;500;700&display=swap" rel="stylesheet">
<style>
  :root {
    --backdrop: #2a2a2c;
    --brand-blue: #0277c2;
    --brand-deep: #3176b5;
    --brand-cyan: #85cae6;
    --brand-pale: #cee9f5;
    --paper: #ffffff;
    --ink: #3a3a3a;
    --rule: #b9b9b9;
  }
  * { margin: 0; padding: 0; box-sizing: border-box; }
  html, body { width: 1200px; height: 874px; overflow: hidden; }
  body {
    background: var(--backdrop);
    font-family: "Roboto", Arial, sans-serif;
    position: relative;
  }
  .card {
    position: absolute;
    left: 290px;
    width: 620px;
    height: 354px;
    box-shadow: 0 10px 30px rgba(0,0,0,.45);
  }
  .card-front {
    top: 52px;
    background: var(--brand-blue);
    display: flex;
    flex-direction: column;
    align-items: center;
    justify-content: center;
    gap: 14px;
  }
  .wordmark {
    display: flex;
    align-items: center;
    gap: 16px;
    color: var(--brand-cyan);
    font-weight: 300;
    font-size: 56px;
    letter-spacing: 8px;
    line-height: 1;
  }
  .wordmark-dot {
    width: 14px; height: 14px;
    background: var(--brand-cyan);
    border-radius: 50%;
  }
  .tagline {
    color: var(--brand-pale);
    font-weight: 500;
    font-size: 15px;
    letter-spacing: 4px;
    padding-left: 30px;
  }
  .card-back {
    top: 462px;
    background: var(--paper);
    border-bottom: 5px solid var(--brand-blue);
  }
  .identity {
    position: absolute;
    right: 352px;
    top: 104px;
    text-align: right;
  }
  .person-name {
    color: var(--brand-blue);
    font-weight: 500;
    font-size: 27px;
    line-height: 1.1;
  }
  .person-title {
    color: var(--ink);
    font-weight: 500;
    font-size: 17px;
    margin-top: 2px;
  }
  .divider {
    position: absolute;
    left: 290px;
    top: 100px;
    width: 1px;
    height: 112px;
    background: var(--rule);
  }
  .contacts {
    position: absolute;
    left: 306px;
    top: 98px;
    list-style: none;
  }
  .contacts li {
    display: flex;
    align-items: center;
    gap: 10px;
    color: var(--ink);
    font-size: 17px;
    line-height: 23px;
  }
  .contacts svg, .address svg { width: 14px; height: 14px; fill: var(--brand-blue); flex: none; }
  .address {
    position: absolute;
    left: 160px;
    top: 262px;
    display: flex;
    align-items: center;
    gap: 10px;
    color: var(--ink);
    font-size: 17px;
    white-space: nowrap;
  }
</style>
</head>
<body>
  <section class="card card-front">
    <div class="wordmark"><span class="wordmark-dot"></span>TARVIMOOR</div>
    <p class="tagline">GMP &amp; JANITORIAL SERVICES</p>
  </section>

  <section class="card card-back">
    <div class="identity">
      <p class="person-name">Daniel Hart</p>
      <p class="person-title">President</p>
    </div>
    <div class="divider"></div>
    <ul class="contacts">
      <li><svg viewBox="0 0 16 16"><path d="M3 1l3 3-2 2c1 2 3 4 5 5l2-2 3 3-2 3C6 14 2 10 1 3z"/></svg>555-214-7730</li>
      <li><svg viewBox="0 0 16 16"><path d="M4 0h8v16H4zM5.5 1.5v11h5v-11z"/></svg>555-618-2094</li>
      <li><svg viewBox="0 0 16 16"><path d="M4 1h8v4H4zM1 6h14v7h-3v2H4v-2H1zM5 10v4h6v-4z"/></svg>555-307-4416</li>
      <li><svg viewBox="0 0 16 16"><path d="M1 3h14v10H1zM2 4.5v.5l6 4 6-4v-.5z"/></svg>info@tarvimoor.com</li>
      <li><svg viewBox="0 0 16 16"><circle cx="8" cy="8" r="7"/></svg>www.tarvimoor.com</li>
    </ul>
    <p class="address"><svg viewBox="0 0 16 16"><path d="M8 0a5.5 5.5 0 0 1 5.5 5.5C13.5 10 8 16 8 16S2.5 10 2.5 5.5A5.5 5.5 0 0 1 8 0zm0 3.5a2 2 0 1 0 0 4 2 2 0 0 0 0-4z"/></svg>4120 Cedar Hollow Road, Fairbanks, Alaska 99701</p>
  </section>
</body>
</html>
```